今まで使っていた名刺がちょうど切れたので、名刺デザインを刷新したいと思っています。社名(すずらん)をイメージした緑のカラーリング、写真、イラスト等をモチーフにしたの提案をいただければと思います。
表面 株式会社すずらん総合企画、森田健税理士・社会保険労務士事務所、代表取締役所長、森田健(MORITAKEN)、〒731-0154広島県広島市安佐南区上安5丁目3番12号ベルクレスト川内3階、TEL022(393)5940、FAX022(393)5941、 e-mail:suzuran-east@kumori-mail.jp
裏面 表面の英字表記
又は
(業務内容)
各種税務申告書作成申告(電子申告)
税務相談
記帳代行、経理代行
社会保険関係書類作成提出(電子申請)
各種助成金申請
生命保険代理店
緑系
特になし

多数の提案ありがとうございます。求めていたイメージ通りの提案でしたので選ばせて頂きました。宜しくお願い致します。

この度は多数の提案ありがとうございます。全て素敵なデザインでしたが社内での協議の上決定させて頂きました。

```html
<!DOCTYPE html>
<html lang="ja">
<head>
<meta charset="utf-8">
<title>森田健 名刺</title>
<link rel="stylesheet" href="https://fonts.googleapis.com/css2?family=Noto+Sans+JP:wght@400;500;700&display=swap">
<style>
:root{
  --green:#2aa345;
  --green-dark:#1f8a37;
  --ink:#2b2b2b;
  --white:#ffffff;
  --page:#ffffff;
  --card-line:#d9d9d9;
}
*{margin:0;padding:0;box-sizing:border-box}
html,body{width:850px;height:1200px;overflow:hidden;background:var(--page)}
body{font-family:"Noto Sans JP",sans-serif;color:var(--ink);position:relative}
.card{position:absolute;left:28px;width:794px;height:480px;overflow:hidden;border:1px solid var(--card-line)}
.card--front{top:110px;background:var(--white)}
.card--back{top:630px;background:var(--green);border-color:var(--green)}
.leaf-area{position:absolute;left:520px;top:26px;width:230px;height:410px;border-radius:8px}
.card--front .leaf-area{background:var(--green)}
.card--back .leaf-area{background:var(--white)}
.services{position:absolute;left:520px;top:26px;width:230px;height:410px;display:flex;flex-direction:column;justify-content:center;align-items:center;list-style:none;padding:0 18px}
.services li{width:100%;text-align:center;font-size:12.5px;line-height:1.35;padding:5px 0;border-bottom:1px solid currentColor}
.services li:last-child{border-bottom:none}
.card--front .services{color:var(--white)}
.card--back .services{color:var(--green-dark)}
.card--back .services li{font-size:11.5px}
.band{position:absolute;left:0;bottom:0;width:100%;height:30px;background:var(--green)}
.identity{position:absolute;left:58px;top:40px}
.title{font-size:13px;font-weight:500}
.name{font-size:38px;font-weight:700;letter-spacing:.08em;line-height:1.25;margin-top:4px}
.name-roman{font-size:12px;color:var(--green);letter-spacing:.12em;border-top:2px solid var(--green);padding-top:3px;width:170px}
.office{position:absolute;left:58px;top:196px;font-size:20px;font-weight:700;line-height:1.4}
.contact{position:absolute;left:58px;top:268px;font-size:13.5px;line-height:1.55}
.card--back .identity{color:var(--white);top:62px}
.card--back .title{font-size:14px;font-weight:400}
.card--back .name{font-size:36px;letter-spacing:.02em;margin-top:0}
.rule{width:390px;height:2px;background:var(--white);margin-top:4px}
.card--back .office{color:var(--white);top:196px;font-size:18px;line-height:1.3}
.card--back .contact{color:var(--white);top:276px;font-size:13.5px;line-height:1.5}
</style>
</head>
<body>
<section class="card card--front" aria-label="名刺 表面">
  <div class="identity">
    <p class="title">代表取締役所長</p>
    <h1 class="name">森田　健</h1>
    <p class="name-roman">MORITA&nbsp;&nbsp;&nbsp;KEN</p>
  </div>
  <div class="office">
    <p>株式会社 すずらん総合企画</p>
    <p>森田健税理士・社会保険労務士事務所</p>
  </div>
  <div class="contact">
    <p>〒731-0154 広島県広島市安佐南区上安5丁目3番12号</p>
    <p>ベルクレスト川内3階</p>
    <p>TEL：082-415-2836　FAX：082-415-2837</p>
    <p>E-mail：suzuran-east@kumori-mail.jp</p>
  </div>
  <div class="leaf-area" role="img" aria-label="緑の葉のイラスト"></div>
  <ul class="services">
    <li>各種税務申告書作成申告<br>(電子申告)</li>
    <li>税務相談</li>
    <li>記帳代行、経理代行</li>
    <li>社会保険関係書類作成提出<br>(電子申請)</li>
    <li>各種助成金申請</li>
    <li>生命保険代理店</li>
  </ul>
  <div class="band"></div>
</section>

<section class="card card--back" aria-label="Business card back">
  <div class="identity">
    <p class="title">Representative Director</p>
    <h2 class="name">Morita Ken</h2>
    <div class="rule"></div>
  </div>
  <div class="office">
    <p>Suzuran Management Co., Ltd.</p>
    <p>Ken Morita Tax accountant and</p>
    <p>social insurance labor consultant office</p>
  </div>
  <div class="contact">
    <p>3rd floor, Bellcrest Kawauchi,</p>
    <p>5-3-12 Kamiyasu, Asaminami-ku,</p>
    <p>Hiroshima City, Hiroshima Prefecture 731-0154</p>
    <p>TEL : 082-415-2836　FAX : 082-415-2837</p>
    <p>E-mail : suzuran-east@kumori-mail.jp</p>
  </div>
  <div class="leaf-area" role="img" aria-label="White leaf illustration"></div>
  <ul class="services">
    <li>Various tax return forms<br>(Electronic filing)</li>
    <li>Tax consultation</li>
    <li>Bookkeeping, accounting</li>
    <li>Submit social insurance documents<br>(Electronic application)</li>
    <li>Apply for various grants</li>
    <li>Life insurance agency</li>
  </ul>
</section>
</body>
</html>
```